LPS AUDITION

I need a post card design (front only) with this on it:
Leap Pulse Stride (this is the main title to be in all caps)
Auditions
Date: Thursday June 30th
6:30-8:30 PM in person
Address: 4172 Kestrel BLVD, Marlow Bay CA 94000
video submissions turn in by Sunday July 3rd, 2022 email:LeapPulseStride22@movenote.test
Teens and Adults welcomed

SO PLEASE COME UP WITH A DESIGN THATS COLORFUL AND INVITING THX!

```html
<!DOCTYPE html>
<html lang="en">
<head>
<meta charset="utf-8">
<title>Leap Pulse Stride Auditions – Postcard</title>
<link href="https://fonts.googleapis.com/css2?family=Bungee+Inline&family=Bebas+Neue&family=Roboto:wght@500;700&family=Oswald:wght@500;600&family=Noto+Serif:wght@700&family=Crimson+Text&display=swap" rel="stylesheet">
<style>
  :root {
    --page: #ffffff;
    --night: #0d0a14;
    --violet: #3a1a4f;
    --magenta: #f04fd8;
    --pink: #ff5fd2;
    --peach: #f2c48e;
    --sky: #4fc6ee;
    --aqua: #7fe0e8;
    --white: #ffffff;
    --ink: #111111;
  }
  * { margin: 0; padding: 0; box-sizing: border-box; }
  html, body { width: 800px; height: 1200px; overflow: hidden; background: var(--page); }
  .canvas { position: relative; width: 800px; height: 1200px; }
  .postcard {
    position: absolute; left: 0; top: 333px; width: 800px; height: 534px;
    overflow: hidden; color: var(--white);
    background:
      radial-gradient(ellipse 260px 90px at 50% 200px, rgba(190,90,220,.45), transparent 70%),
      radial-gradient(ellipse 420px 120px at 50% 500px, rgba(150,60,180,.45), transparent 70%),
      radial-gradient(ellipse 200px 160px at 15% 420px, rgba(60,130,180,.35), transparent 70%),
      radial-gradient(ellipse 200px 160px at 88% 430px, rgba(60,130,180,.3), transparent 70%),
      linear-gradient(180deg, var(--night) 0%, #150f22 45%, var(--violet) 100%);
  }
  .crowd { position: absolute; bottom: 0; }
  .crowd--left { left: 0; width: 130px; height: 170px;
    background: linear-gradient(180deg, transparent, rgba(28,22,48,.9)); }
  .crowd--right { right: 0; width: 160px; height: 150px;
    background: linear-gradient(180deg, transparent, rgba(28,22,48,.9)); }
  .sparkle-dots { position: absolute; display: flex; gap: 4px; }
  .sparkle-dots span { width: 4px; height: 4px; background: var(--magenta); }
  .title {
    position: absolute; left: 0; width: 800px; top: 66px; text-align: center;
    font-family: "Bungee Inline", sans-serif; font-size: 60px; line-height: 1;
    letter-spacing: -1px; white-space: nowrap;
  }
  .title .w1 { color: var(--pink); }
  .title .w2 { color: var(--peach); }
  .title .w3 { color: var(--sky); }
  .subtitle {
    position: absolute; left: 0; width: 800px; top: 134px; text-align: center;
    font-family: "Bebas Neue", sans-serif; font-size: 58px; line-height: 1;
    letter-spacing: 8px; color: transparent; -webkit-text-stroke: 1.5px var(--aqua);
  }
  .badge {
    position: absolute; left: 659px; top: 161px; width: 86px; height: 86px; border-radius: 50%;
    background: radial-gradient(circle at 50% 40%, #ff7ee0, #e83fc4);
    border: 2px solid #ffd2f2; display: flex; align-items: center; justify-content: center;
    text-align: center; font-family: "Oswald", sans-serif; font-weight: 600;
    font-size: 15px; line-height: 1.05; color: var(--white);
  }
  .date { position: absolute; left: 119px; top: 232px; font-family: "Roboto", sans-serif; font-weight: 700; line-height: 1; }
  .date .day-num { display: block; font-size: 40px; color: var(--sky); }
  .date .weekday { display: block; font-size: 40px; color: var(--white); margin-top: 2px; }
  .sparkle { position: absolute; left: 368px; top: 238px; width: 24px; height: 24px; }
  .time-box {
    position: absolute; left: 400px; top: 236px; width: 281px; height: 46px;
    border: 2px solid var(--white); display: flex; align-items: center; justify-content: center;
    font-family: "Bebas Neue", sans-serif; font-size: 32px; gap: 8px;
  }
  .time-box .time { color: var(--sky); }
  .address {
    position: absolute; left: 398px; top: 288px; width: 286px; height: 21px;
    background: var(--aqua); color: var(--ink); border: 1px solid var(--magenta);
    font-family: "Roboto", sans-serif; font-weight: 500; font-size: 12.5px;
    display: flex; align-items: center; justify-content: center; white-space: nowrap;
  }
  .submission {
    position: absolute; left: 198px; top: 348px; width: 405px; height: 81px;
    border: 1px solid var(--sky); border-top: none;
  }
  .submission::before, .submission::after {
    content: ""; position: absolute; top: 0; height: 1px; width: 22px; background: var(--sky);
  }
  .submission::before { left: 0; }
  .submission::after { right: 0; }
  .submission .lead {
    position: absolute; left: 0; width: 100%; top: -11px; text-align: center;
    font-family: "Roboto", sans-serif; font-weight: 500; font-size: 20px; color: var(--peach);
  }
  .submission .deadline {
    position: absolute; left: 0; width: 100%; top: 16px; text-align: center;
    font-family: "Bebas Neue", sans-serif; font-size: 40px; color: var(--sky); line-height: 1;
  }
  .submission .weekday-tag {
    position: absolute; left: 130px; top: 57px; width: 144px; height: 31px;
    background: var(--magenta); color: var(--ink); text-align: center;
    font-family: "Noto Serif", serif; font-weight: 700; font-size: 24px; line-height: 31px;
  }
  .email {
    position: absolute; left: 270px; top: 481px; width: 260px; height: 26px;
    border: 1px solid var(--white); display: flex; align-items: center; justify-content: center;
    font-family: "Crimson Text", serif; font-size: 15px; letter-spacing: .3px; white-space: nowrap;
  }
</style>
</head>
<body>
<main class="canvas">
  <section class="postcard" aria-label="Leap Pulse Stride auditions postcard">
    <div class="crowd crowd--left" role="img" aria-label="Silhouettes of a cheering crowd"></div>
    <div class="crowd crowd--right" role="img" aria-label="Silhouettes of a cheering crowd"></div>

    <div class="sparkle-dots" style="left:11px;top:89px"><span></span><span></span><span></span><span></span><span></span><span></span></div>
    <div class="sparkle-dots" style="left:22px;top:58px"><span></span><span></span></div>
    <div class="sparkle-dots" style="left:739px;top:128px"><span></span><span></span><span></span><span></span></div>
    <div class="sparkle-dots" style="left:439px;top:222px"><span></span><span></span><span></span><span></span><span></span><span></span><span></span></div>
    <div class="sparkle-dots" style="left:33px;top:192px"><span></span><span></span></div>
    <div class="sparkle-dots" style="left:733px;top:251px"><span></span><span></span></div>
    <div class="sparkle-dots" style="left:33px;top:364px"><span></span><span></span><span></span><span></span><span></span><span></span></div>
    <div class="sparkle-dots" style="left:637px;top:364px"><span></span><span></span><span></span><span></span><span></span><span></span></div>
    <div class="sparkle-dots" style="left:118px;top:425px"><span></span><span></span><span></span><span></span><span></span><span></span></div>
    <div class="sparkle-dots" style="left:715px;top:421px"><span></span><span></span><span></span><span></span><span></span><span></span></div>

    <h1 class="title"><span class="w1">LEAP</span> <span class="w2">PULSE</span> <span class="w3">STRIDE</span></h1>
    <h2 class="subtitle">AUDITIONS</h2>

    <div class="badge">TEENS<br>&amp; ADULTS<br>WELCOMED</div>

    <p class="date"><span class="day-num">JUNE 30TH</span><span class="weekday">THURSDAY</span></p>

    <svg class="sparkle" viewBox="0 0 24 24" aria-hidden="true">
      <path d="M9 2 L11 9 L18 11 L11 13 L9 20 L7 13 L0 11 L7 9 Z" fill="#fff"/>
      <path d="M19 12 L20 15 L23 16 L20 17 L19 20 L18 17 L15 16 L18 15 Z" fill="#fff"/>
    </svg>

    <div class="time-box"><span class="time">6:30-8:30 PM</span><span class="mode">IN PERSON</span></div>
    <p class="address">4172 Kestrel BLVD, Marlow Bay CA 94000</p>

    <div class="submission">
      <p class="lead">VIDEO SUBMISSIONS TURN IN BY</p>
      <p class="deadline">JULY 3RD, 2022</p>
      <p class="weekday-tag">SUNDAY</p>
    </div>

    <p class="email">LeapPulseStride22@movenote.test</p>
  </section>
</main>
</body>
</html>
```